I need bigcommerce design template

hi, am looking for a quality, professional, attractive and mature bigcommerce template for my site. My site will sell clothes and bags and shoes. Basically what you are to do is setup the store. I have domain name which hostwren will attach them self.

```html
<!DOCTYPE html>
<html lang="en">
<head>
<meta charset="utf-8">
<title>Marlo — Clothing, Bags &amp; Shoes</title>
<link href="https://fonts.googleapis.com/css2?family=Open+Sans:wght@400;600;700&family=Montserrat:wght@400;700&display=swap" rel="stylesheet">
<style>
:root{
  --ink:#222222;
  --ink-soft:#555555;
  --muted:#999999;
  --line:#e3e3e3;
  --orange:#f26a2a;
  --paper:#ffffff;
  --hero-bg:#ececec;
  --band:#f1f1f1;
  --brown:#a08478;
  --footer:#1e1e1e;
  --footer-text:#9a9a9a;
}
*{box-sizing:border-box;margin:0;padding:0}
html,body{width:1200px;height:3000px;overflow:hidden}
body{background:var(--paper);font-family:"Open Sans",Arial,sans-serif;color:var(--ink);position:relative}
.container{position:absolute;left:185px;width:830px}
.fill{display:block}

/* header */
.site-header{position:absolute;top:0;left:0;width:1200px;height:48px;background:var(--ink)}
.logo{position:absolute;left:225px;top:12px;color:#fff;font-weight:700;font-size:20px;display:flex;align-items:center;gap:8px}
.logo .dot{width:10px;height:10px;border-radius:50%;background:var(--orange)}
.main-nav{position:absolute;left:358px;top:0;display:flex;height:48px}
.main-nav a{color:#ddd;text-decoration:none;font-size:11px;font-weight:600;padding:0 16px;line-height:48px}
.main-nav a.active{background:#3a3a3a;color:#fff}
.search{position:absolute;right:185px;top:14px;width:130px;height:20px;border:1px solid #555;color:#888;font-size:10px;padding:3px 8px}

/* hero */
.hero{position:absolute;top:48px;left:0;width:1200px;height:442px;background:var(--hero-bg)}
.hero-photo{position:absolute;left:185px;top:0;width:520px;height:442px;background:linear-gradient(90deg,#e6e3e0,#d9c9c4 40%,#cfd8d2 80%,#ececec)}
.hero-copy{position:absolute;left:820px;top:92px;width:200px}
.hero-copy h2{color:var(--orange);font-family:Montserrat,sans-serif;font-size:20px;font-weight:700;line-height:1.2}
.hero-copy p{font-size:10px;color:var(--ink-soft);line-height:1.6;margin:12px 0 18px}
.btn-dark{display:inline-block;background:var(--ink);color:#fff;font-size:11px;padding:7px 20px}

/* features */
.features{position:absolute;top:490px;left:0;width:1200px;height:50px;background:var(--band);display:flex;justify-content:center;gap:120px;align-items:center}
.feature{display:flex;align-items:center;gap:10px;font-size:9px;font-weight:700;color:var(--ink-soft)}

/* categories */
.categories{top:592px;display:flex;gap:17px}
.category{position:relative;width:265px;height:160px}
.category span{position:absolute;inset:0;display:flex;align-items:center;justify-content:center;color:#fff;font-family:Montserrat,sans-serif;font-weight:700;font-size:14px;letter-spacing:1px}

/* section titles */
.section-title{position:absolute;left:185px;width:830px;text-align:center}
.section-title h3{font-family:Montserrat,sans-serif;font-size:15px;font-weight:700}
.section-title p{color:var(--orange);font-size:9px;margin-top:4px}
.tabs{display:flex;justify-content:center;margin-top:12px}
.tabs span{font-size:9px;padding:4px 16px;background:#eee;color:#666}
.tabs span.on{background:var(--ink);color:#fff}

/* products */
.products{display:flex;gap:20px}
.product{width:150px}
.product .fill{width:150px;height:220px}
.product h4{font-size:9px;font-weight:400;color:var(--ink-soft);margin-top:10px}
.product .price{font-size:10px;color:var(--orange);margin-top:4px}
.badge{position:absolute;margin:8px 0 0 116px;width:28px;height:28px;border-radius:50%;background:var(--orange);color:#fff;font-size:8px;display:flex;align-items:center;justify-content:center}

/* promo banners */
.promos{top:1180px;display:flex;gap:16px}
.promo{position:relative;width:407px;height:140px;display:flex;flex-direction:column;align-items:center;justify-content:center;color:#fff}
.promo.men{background:linear-gradient(90deg,#2e3a44,#5a6670)}
.promo.new{background:var(--orange)}
.promo h3{font-family:Montserrat,sans-serif;font-size:18px;font-weight:400;letter-spacing:1px}
.promo .btn{margin-top:10px;font-size:9px;padding:5px 14px;background:var(--orange);color:#fff}
.promo.new .btn{background:#fff;color:var(--orange)}

/* sale */
.sale{top:1752px;height:316px;background:#1d1d1d}
.sale .shoe-shot{position:absolute;left:63px;top:68px;width:292px;height:180px;background:linear-gradient(135deg,#4a4440,#8c5b4e 60%,#c27a60)}
.sale .bg-shot{position:absolute;right:0;top:0;width:420px;height:316px;background:linear-gradient(90deg,#1d1d1d,#3b2d2e 50%,#5e3f3f)}
.sale-copy{position:absolute;left:420px;top:98px;color:#fff;width:300px}
.sale-copy .lead{font-size:14px;color:#ddd}
.sale-copy h3{font-family:Montserrat,sans-serif;font-size:22px;font-weight:400;margin-top:4px}
.sale-copy p{font-size:9px;color:#aaa;margin-top:8px;line-height:1.6}
.sale-copy .link{color:var(--orange);font-size:9px;font-weight:700;margin-top:10px}
.dots{display:flex;gap:6px;justify-content:center}
.dots i{width:6px;height:6px;border-radius:50%;background:#777}
.dots i.on{background:var(--orange)}

/* blog */
.blog{top:2180px;display:flex;gap:17px}
.post{width:265px}
.post .fill{height:100px}
.post .meta{display:flex;gap:12px;margin-top:12px}
.post time{font-size:8px;color:var(--muted);width:40px;line-height:1.4}
.post h4{font-size:9px;font-weight:600;color:var(--ink-soft);line-height:1.5}

/* brands */
.brands{top:2460px;height:64px;border-top:1px solid var(--line);border-bottom:1px solid var(--line);display:flex;justify-content:space-around;align-items:center}
.brand{display:flex;align-items:center;gap:8px;color:#888;font-weight:700;font-size:14px}
.brand i{width:12px;height:12px;border-radius:50%;background:#aaa}

/* newsletter */
.newsletter{position:absolute;top:2580px;left:0;width:1200px;height:100px;background:var(--brown);text-align:center;color:#fff}
.newsletter h3{font-size:10px;font-weight:700;margin-top:24px;letter-spacing:1px}
.newsletter form{display:flex;justify-content:center;margin-top:12px}
.newsletter .field{width:340px;height:22px;background:#fff;color:#999;font-size:9px;text-align:left;padding:5px 8px}
.newsletter .btn{height:22px;background:var(--orange);font-size:9px;padding:5px 14px}

/* footer */
.site-footer{position:absolute;top:2680px;left:0;width:1200px;height:320px;background:var(--footer);color:var(--footer-text);font-size:9px}
.footer-logo{position:absolute;left:185px;top:44px;color:#fff;font-weight:700;font-size:20px;display:flex;align-items:center;gap:8px}
.footer-logo .dot{width:10px;height:10px;border-radius:50%;background:var(--orange)}
.footer-about{position:absolute;left:185px;top:84px;width:150px;line-height:1.6}
.footer-col{position:absolute;top:44px;width:120px}
.footer-col h5{color:#fff;font-size:9px;font-weight:700;margin-bottom:10px}
.footer-col li{list-style:none;line-height:1.9}
.mini{display:flex;gap:8px;align-items:center;margin-bottom:8px}
.mini i{width:26px;height:26px;background:#6b5b55}
.contact{position:absolute;left:850px;top:44px;width:170px;line-height:2}
.payments{position:absolute;left:0;top:232px;width:1200px;display:flex;justify-content:center;gap:6px}
.payments i{width:30px;height:18px;border-radius:2px;background:#8a8a8a}
.payments i:nth-child(2){background:#5d7fa6}
.payments i:nth-child(3){background:#a8793f}
.copyright{position:absolute;left:0;top:268px;width:1200px;text-align:center;font-size:8px;color:#777}
</style>
</head>
<body>

<header class="site-header">
  <div class="logo"><span class="dot"></span>Marlo</div>
  <nav class="main-nav"><a class="active">HOME</a><a>WOMEN</a><a>MEN</a><a>BAG</a><a>CONTACT</a></nav>
  <div class="search">Search</div>
</header>

<section class="hero">
  <div class="hero-photo fill" role="img" aria-label="Three women modelling the new season outfits"></div>
  <div class="hero-copy">
    <h2>20% OFF NEW SEASON</h2>
    <p>Refresh your wardrobe with our spring edit of dresses, denim and soft layers. Free returns on every order.</p>
    <span class="btn-dark">Shop Now</span>
  </div>
</section>

<section class="features">
  <div class="feature"><svg width="22" height="14" viewBox="0 0 22 14"><rect x="1" y="2" width="12" height="8" fill="#555"/><path d="M13 5h5l3 3v2h-8z" fill="#555"/><circle cx="5" cy="11.5" r="2" fill="#555"/><circle cx="17" cy="11.5" r="2" fill="#555"/></svg>FREE SHIPPING AND DELIVERY</div>
  <div class="feature"><svg width="20" height="14" viewBox="0 0 20 14"><rect x="1" y="1" width="18" height="12" rx="2" fill="none" stroke="#555" stroke-width="1.5"/><rect x="1" y="4" width="18" height="2.5" fill="#555"/></svg>SECURE PAYMENT GATEWAYS</div>
  <div class="feature"><svg width="16" height="16" viewBox="0 0 16 16"><path d="M8 1l6 2v5c0 4-3 6-6 7-3-1-6-3-6-7V3z" fill="#555"/><path d="M5 8l2 2 4-4" stroke="#fff" stroke-width="1.5" fill="none"/></svg>MONEY BACK GUARANTEE</div>
</section>

<section class="container categories">
  <div class="category"><div class="fill" style="height:160px;background:linear-gradient(135deg,#8a7466,#c2b4a8)" role="img" aria-label="Pair of suede shoes"></div><span>SHOES</span></div>
  <div class="category"><div class="fill" style="height:160px;background:linear-gradient(135deg,#6b6b6b,#b0aaa6)" role="img" aria-label="Models in stylish outfits"></div><span>STYLISH CLOTHING</span></div>
  <div class="category"><div class="fill" style="height:160px;background:linear-gradient(135deg,#7a6a62,#c4b6ad)" role="img" aria-label="Women carrying handbags"></div><span>HANDBAG</span></div>
</section>

<div class="section-title" style="top:784px">
  <h3>LATEST PRODUCTS</h3><p>Fresh picks added every week</p>
  <div class="tabs"><span class="on">New</span><span>Featured</span><span>Sale</span></div>
</div>
<section class="container products" style="top:880px">
  <div class="product"><div class="fill" style="background:linear-gradient(#eeeeee,#3a3a3a 60%,#eeeeee)" role="img" aria-label="Model in black graphic dress"></div><h4>Slim Cotton Blouse</h4><div class="price">$ 49.00</div></div>
  <div class="product"><span class="badge">SALE</span><div class="fill" style="background:linear-gradient(#f0f0f0,#e05a9c 55%,#f0f0f0)" role="img" aria-label="Model in pink chiffon top"></div><h4>Pink Chiffon Top</h4><div class="price">$ 39.00</div></div>
  <div class="product"><div class="fill" style="background:linear-gradient(#efefef,#b89a6a 55%,#efefef)" role="img" aria-label="Model in gold sequin dress"></div><h4>Gold Sequin Dress</h4><div class="price">$ 89.00</div></div>
  <div class="product"><div class="fill" style="background:linear-gradient(#f0f0f0,#d8363a 55%,#f0f0f0)" role="img" aria-label="Model in red shift dress"></div><h4>Red Shift Dress</h4><div class="price">$ 59.00</div></div>
  <div class="product"><div class="fill" style="background:linear-gradient(#f0f0f0,#a8a29e 55%,#f0f0f0)" role="img" aria-label="Model in grey knit cardigan"></div><h4>Grey Knit Cardigan</h4><div class="price">$ 45.00</div></div>
</section>

<section class="container promos">
  <div class="promo men" role="img" aria-label="Menswear city scene"><h3>MENSWEAR 2016</h3><span class="btn">Shop collection</span></div>
  <div class="promo new"><h3>NEWEST COLLECTION</h3><span class="btn">View more</span></div>
</section>

<div class="section-title" style="top:1368px">
  <h3>TOP RATED PRODUCTS</h3><p>Loved most by our shoppers</p>
  <div class="tabs"><span class="on">New</span><span>Featured</span><span>Sale</span></div>
</div>
<section class="container products" style="top:1460px">
  <div class="product"><div class="fill" style="height:212px;background:linear-gradient(#f0f0f0,#c0262c 60%,#f0f0f0)" role="img" aria-label="Model with red leather bag"></div><h4>Red Leather Tote</h4><div class="price">$ 79.00</div></div>
  <div class="product"><div class="fill" style="height:212px;background:linear-gradient(#f0f0f0,#b5a590 60%,#f0f0f0)" role="img" aria-label="Model with beige handbag"></div><h4>Beige Structured Bag</h4><div class="price">$ 69.00</div></div>
  <div class="product"><div class="fill" style="height:212px;background:linear-gradient(#f0f0f0,#8c6a54 60%,#f0f0f0)" role="img" aria-label="Model with brown shoulder bag"></div><h4>Brown Shoulder Bag</h4><div class="price">$ 65.00</div></div>
  <div class="product"><div class="fill" style="height:212px;background:linear-gradient(#f0f0f0,#c59a62 60%,#f0f0f0)" role="img" aria-label="Model with tan handbag"></div><h4>Tan Mini Handbag</h4><div class="price">$ 55.00</div></div>
  <div class="product"><div class="fill" style="height:212px;background:linear-gradient(#f0f0f0,#b8452e 60%,#f0f0f0)" role="img" aria-label="Model with rust red purse"></div><h4>Rust Clasp Purse</h4><div class="price">$ 59.00</div></div>
</section>

<section class="container sale">
  <div class="bg-shot" role="img" aria-label="Woman in heels on dark backdrop"></div>
  <div class="shoe-shot" role="img" aria-label="Fashion magazine with pair of high heels"></div>
  <div class="sale-copy">
    <div class="lead">End of season</div>
    <h3>Sale for women collection</h3>
    <p>Up to half off selected dresses, shoes and bags this month.</p>
    <div class="link">DISCOVER OUR COLLECTION</div>
  </div>
  <div class="dots" style="position:absolute;left:0;right:0;bottom:20px"><i class="on"></i><i></i><i></i></div>
</section>

<div class="section-title" style="top:2112px">
  <h3>FROM OUR BLOG</h3><p>News, tips and style notes from our team</p>
</div>
<section class="container blog">
  <article class="post"><div class="fill" style="background:linear-gradient(90deg,#3d3a3a,#9b8c86)" role="img" aria-label="Runway fashion show"></div><div class="meta"><time>08 May 2016</time><h4>Styling tips for spring layers</h4></div></article>
  <article class="post"><div class="fill" style="background:linear-gradient(90deg,#6e2a2a,#c4a48a)" role="img" aria-label="Red handbag close up"></div><div class="meta"><time>12 May 2016</time><h4>Choosing the right everyday bag</h4></div></article>
  <article class="post"><div class="fill" style="background:linear-gradient(90deg,#d8d2cc,#5e4a40)" role="img" aria-label="Legs in boots on pavement"></div><div class="meta"><time>20 May 2016</time><h4>Boots that carry you through</h4></div></article>
</section>
<div class="dots" style="position:absolute;top:2400px;left:0;width:1200px"><i></i><i class="on"></i><i></i></div>

<section class="container brands">
  <div class="brand"><i></i>Calverne</div>
  <div class="brand"><i></i>Sorrel</div>
  <div class="brand"><i></i>Melvora</div>
  <div class="brand"><i></i>Sorrel</div>
  <div class="brand"><i></i>Melvora</div>
</section>

<section class="newsletter">
  <h3>JOIN OUR NEWSLETTER</h3>
  <form><div class="field">Your email address</div><div class="btn">Sign up</div></form>
</section>

<footer class="site-footer">
  <div class="footer-logo"><span class="dot"></span>Marlo</div>
  <p class="footer-about">We design timeless pieces for everyday wear, made to last.</p>
  <div class="footer-col" style="left:395px"><h5>INFORMATION</h5><ul><li>About Us</li><li>Delivery Info</li><li>Privacy Policy</li><li>Terms of Use</li></ul></div>
  <div class="footer-col" style="left:510px"><h5>OUR SERVICES</h5><ul><li>My Account</li><li>Order History</li><li>Wish List</li><li>Returns</li></ul></div>
  <div class="footer-col" style="left:625px"><h5>MAIN LINK</h5><ul><li>Home</li><li>Women</li><li>Men</li><li>Bags</li></ul></div>
  <div class="footer-col" style="left:730px;width:110px"><h5>PRODUCT</h5>
    <div class="mini"><i role="img" aria-label="Linen dress thumbnail"></i>Linen Dress</div>
    <div class="mini"><i role="img" aria-label="Leather tote thumbnail"></i>Leather Tote</div>
  </div>
  <div class="contact">
    <div>120 Harbor Street, Lakeview City</div>
    <div>+1 555 014 2288</div>
    <div>hello@marlostore.com</div>
  </div>
  <div class="payments"><i></i><i></i><i></i><i></i><i></i></div>
  <div class="copyright">© 2016 Marlo. All rights reserved.</div>
</footer>

</body>
</html>
```